Fun label for kids Afro and curly hair brand

A label for a 250 ml Boston bottle. For a moisturiser detangler and leave in conditioner formulated for kids to help with pain free detangling and provide maximum moisture and conditioner. We want children with this hair texture to love their hair.
Target Market(s)
Afro and curly haired children and their parents
Industry/Entity Type
Beauty and cosmetics
Font styles to use
Serif
Colors
Designer to choose colors to be used in the design.
Requirements
Must have
- Logo.Developed for especially children. Label must be wound round the bottle with a right hand leading edge on a 76mm core. Must state the product is free from parabens, sulphates.
Nice to have
- Stand out colours.
Should not have
- N. A

```html
<!DOCTYPE html>
<html lang="en">
<head>
<meta charset="utf-8">
<title>Coilbloom – Detangler Label</title>
<link href="https://fonts.googleapis.com/css2?family=Cormorant+Garamond:wght@500&family=Montserrat:wght@400;600&display=swap" rel="stylesheet">
<style>
  :root {
    --page: #ffffff;
    --label-purple: #7d1d8f;
    --label-purple-light: #9a33ac;
    --leaf-dark: #240a2c;
    --leaf-mid: #4d1659;
    --accent-orange: #d6731b;
    --text-light: #f3e6f5;
    --text-soft: #c9a9d0;
  }
  html, body {
    margin: 0;
    padding: 0;
    width: 1200px;
    height: 857px;
    overflow: hidden;
    background: var(--page);
  }
  .canvas {
    position: relative;
    width: 1200px;
    height: 857px;
  }
  .label-panel {
    position: absolute;
    top: 118px;
    width: 320px;
    height: 620px;
  }
  .label-panel--front { left: 226px; }
  .label-panel--back { left: 657px; }
  .panel-art {
    position: absolute;
    inset: 0;
    width: 320px;
    height: 620px;
  }
  .brand-mark {
    position: absolute;
    left: 0;
    width: 320px;
    padding-left: 10px;
    box-sizing: border-box;
    text-align: center;
    color: var(--text-light);
  }
  .brand-name {
    font-family: "Cormorant Garamond", serif;
    font-weight: 500;
    font-size: 26px;
    line-height: 1;
  }
  .brand-descriptor {
    font-family: "Montserrat", sans-serif;
    font-weight: 400;
    font-size: 7px;
    letter-spacing: 0.3px;
    margin-top: 6px;
    color: var(--text-soft);
  }
  .label-panel--front .brand-mark { top: 172px; }
  .label-panel--back .brand-mark { top: 154px; }
  .label-panel--back .brand-name { font-size: 21px; }
  .label-panel--back .brand-descriptor { font-size: 6px; margin-top: 5px; }
  .free-from-badge {
    position: absolute;
    left: 36px;
    top: 262px;
    background: var(--accent-orange);
    color: #fff;
    font-family: "Montserrat", sans-serif;
    font-weight: 600;
    font-size: 6.5px;
    line-height: 1.25;
    padding: 5px 8px 5px 5px;
    border-radius: 2px;
  }
  .ingredients {
    position: absolute;
    left: 68px;
    top: 236px;
    width: 96px;
    font-family: "Montserrat", sans-serif;
    font-size: 5px;
    line-height: 1.55;
    color: var(--text-soft);
  }
  .ingredients h3, .usage-table h3 {
    margin: 0 0 5px;
    font-size: 5px;
    font-weight: 600;
    color: var(--text-light);
    letter-spacing: 0.5px;
  }
  .ingredients ul { list-style: none; margin: 0; padding: 0; }
  .usage-table {
    position: absolute;
    left: 170px;
    top: 236px;
    width: 88px;
    font-family: "Montserrat", sans-serif;
    font-size: 4.5px;
    line-height: 1.5;
    color: var(--text-soft);
  }
  .usage-table p { margin: 0 0 6px; }
  .usage-icons {
    position: absolute;
    left: 170px;
    top: 380px;
    display: flex;
    gap: 8px;
    font-family: "Montserrat", sans-serif;
    font-size: 5px;
    color: var(--text-light);
    align-items: center;
  }
</style>
</head>
<body>
<main class="canvas">

  <section class="label-panel label-panel--front">
    <svg class="panel-art" viewBox="0 0 320 620">
      <defs>
        <linearGradient id="labelStock" x1="0" x2="1" y1="0" y2="0">
          <stop offset="0" stop-color="var(--label-purple)"/>
          <stop offset="0.7" stop-color="var(--label-purple-light)"/>
          <stop offset="1" stop-color="var(--label-purple)"/>
        </linearGradient>
        <linearGradient id="leafFill" x1="0" x2="1" y1="0" y2="0">
          <stop offset="0" stop-color="var(--leaf-dark)"/>
          <stop offset="1" stop-color="var(--leaf-mid)"/>
        </linearGradient>
        <linearGradient id="illustrationTone" x1="0" x2="1" y1="0" y2="1">
          <stop offset="0" stop-color="#5a3224"/>
          <stop offset="0.6" stop-color="#8a5338"/>
          <stop offset="1" stop-color="#c99aa8"/>
        </linearGradient>
        <clipPath id="leafClipFront">
          <path d="M170 30 C190 120 290 190 285 320 C280 430 200 520 150 575 C70 500 35 420 40 330 C45 220 120 110 170 30 Z"/>
        </clipPath>
      </defs>
      <rect width="320" height="620" fill="url(#labelStock)"/>
      <path d="M170 30 C190 120 290 190 285 320 C280 430 200 520 150 575 C70 500 35 420 40 330 C45 220 120 110 170 30 Z" fill="url(#leafFill)"/>
      <g clip-path="url(#leafClipFront)">
        <rect x="118" y="318" width="160" height="260" rx="70" fill="url(#illustrationTone)" role="img" aria-label="Illustration of a smiling young girl with curly hair in a patterned dress"/>
      </g>
      <path d="M170 30 C190 120 290 190 285 320 C280 430 200 520 150 575 C70 500 35 420 40 330 C45 220 120 110 170 30 Z" fill="none" stroke="var(--accent-orange)" stroke-width="3"/>
    </svg>
    <div class="brand-mark">
      <div class="brand-name">Coilbloom</div>
      <div class="brand-descriptor">Detangler &amp; Leave-In</div>
    </div>
    <div class="free-from-badge">FREE FROM<br>PARABENS, SULPHATES</div>
  </section>

  <section class="label-panel label-panel--back">
    <svg class="panel-art" viewBox="0 0 320 620">
      <defs>
        <linearGradient id="labelStockBack" x1="0" x2="1" y1="0" y2="0">
          <stop offset="0" stop-color="var(--label-purple)"/>
          <stop offset="0.7" stop-color="var(--label-purple-light)"/>
          <stop offset="1" stop-color="var(--label-purple)"/>
        </linearGradient>
        <linearGradient id="leafFillBack" x1="0" x2="1" y1="0" y2="0">
          <stop offset="0" stop-color="var(--leaf-dark)"/>
          <stop offset="1" stop-color="var(--leaf-mid)"/>
        </linearGradient>
      </defs>
      <rect width="320" height="620" fill="url(#labelStockBack)"/>
      <path d="M170 30 C190 120 290 190 285 320 C280 430 200 520 150 575 C70 500 35 420 40 330 C45 220 120 110 170 30 Z" fill="url(#leafFillBack)" stroke="var(--accent-orange)" stroke-width="3"/>
    </svg>
    <div class="brand-mark">
      <div class="brand-name">Coilbloom</div>
      <div class="brand-descriptor">Detangler &amp; Leave-In</div>
    </div>
    <div class="ingredients">
      <h3>INGREDIENTS</h3>
      <ul>
        <li>Aqua (Water)</li>
        <li>Cetearyl Alcohol</li>
        <li>Behentrimonium Chloride</li>
        <li>Glycerin</li>
        <li>Coconut Oil</li>
        <li>Shea Butter</li>
        <li>Castor Seed Oil</li>
        <li>Aloe Leaf Juice</li>
        <li>Hydrolyzed Wheat Protein</li>
        <li>Panthenol</li>
        <li>Parfum</li>
        <li>Sodium Benzoate</li>
        <li>Potassium Sorbate</li>
        <li>Tocopherol</li>
        <li>Citric Acid</li>
      </ul>
    </div>
    <div class="usage-table">
      <h3>DIRECTIONS</h3>
      <p>Spray onto damp hair.<br>Detangle gently with fingers.<br>Leave in, do not rinse.</p>
      <h3>CAUTION</h3>
      <p>For external use only.<br>Keep away from eyes.</p>
    </div>
    <div class="usage-icons">
      <svg width="12" height="16" viewBox="0 0 12 16" aria-hidden="true">
        <rect x="1" y="1" width="10" height="14" fill="none" stroke="var(--text-light)" stroke-width="1"/>
        <rect x="3" y="8" width="6" height="5" fill="var(--text-light)"/>
      </svg>
      <span>250 ml</span>
      <svg width="16" height="14" viewBox="0 0 16 14" aria-hidden="true">
        <path d="M2 5 L14 5 L13 13 L3 13 Z M2 5 L12 1" fill="none" stroke="var(--text-light)" stroke-width="1"/>
      </svg>
      <span>12M</span>
    </div>
  </section>

</main>
</body>
</html>
```